Clerical Business Card Design

I have just started a new business focusing on Clerical / Administration Support for Small to Medium sized Businesses. I can provide support not just only my local area but anywhere as long as it is able to be done over the internet/email. I am the only person working in the business.
I would like to see some designs that are bright in colour yet a clean fresh design. The design should communicate balance.
Updates

Target Market(s)

Small to Medium sized Professional Businesses

Industry/Entity Type

Business

Contact Information for Business Card

Business Name: Vormley's Clerical
Statement: Providing Balanced Efficient Support
My Name: Ilsa Vormley
Phone: 0418 571 924 or 02 6519 4027
Email: vormleysclerical@plimmet.com.au

Colors

Designer to choose colors to be used in the design.

Requirements
Must have
• I'm open to suggestions
Nice to have
• I would like to see maybe something done with the two "C" in the business name whether that could be a focus of difference
Should not have
• Cartoon type pictures

```html
<!DOCTYPE html>
<html lang="en">
<head>
<meta charset="utf-8">
<title>Vormley's Clerical – Business Card</title>
<link rel="stylesheet" href="https://fonts.googleapis.com/css2?family=Open+Sans:wdth,wght@75..100,600&family=Roboto+Condensed:wght@400;700&display=swap">
<style>
  :root {
    --page-bg: #8f9094;
    --card-white: #ffffff;
    --brand-blue: #2759a6;
    --ink-dark: #353535;
    --ink-text: #2e2e2e;
  }
  * { box-sizing: border-box; margin: 0; padding: 0; }
  html, body {
    width: 1200px;
    height: 1000px;
    overflow: hidden;
    background: var(--page-bg);
  }
  .business-card {
    position: absolute;
    left: 274px;
    top: 303px;
    width: 651px;
    height: 393px;
    background: var(--card-white);
    overflow: hidden;
  }
  .brand-panel {
    position: absolute;
    left: 0;
    top: 0;
    width: 224px;
    height: 100%;
    background: var(--brand-blue);
  }
  .panel-tail {
    position: absolute;
    left: 224px;
    top: 137px;
  }
  .brand-mark {
    position: absolute;
    left: 37px;
    top: 85px;
  }
  .brand-text {
    position: absolute;
    right: 41px;
    width: 345px;
    text-align: right;
    white-space: nowrap;
  }
  .company-name {
    top: 94px;
    font-family: "Open Sans", sans-serif;
    font-stretch: 75%;
    font-weight: 600;
    font-size: 46px;
    letter-spacing: -0.5px;
    line-height: 1;
    color: var(--ink-dark);
    text-transform: uppercase;
  }
  .tagline {
    top: 146px;
    font-family: "Roboto Condensed", sans-serif;
    font-weight: 400;
    font-size: 21px;
    line-height: 1;
    color: var(--brand-blue);
  }
  .contact-block {
    position: absolute;
    right: 41px;
    top: 240px;
    text-align: right;
    font-family: "Roboto Condensed", sans-serif;
  }
  .person-name {
    font-weight: 700;
    font-size: 22px;
    line-height: 1;
    color: var(--brand-blue);
    margin-bottom: 26px;
  }
  .contact-line {
    display: flex;
    justify-content: flex-end;
    align-items: center;
    gap: 7px;
    font-size: 18px;
    line-height: 23.5px;
    color: var(--ink-text);
  }
  .contact-icon { fill: var(--brand-blue); }
</style>
</head>
<body>
  <div class="business-card">
    <div class="brand-panel">
      <svg class="brand-mark" width="100" height="100" viewBox="0 0 100 100" aria-hidden="true">
        <circle cx="50" cy="45" r="38" fill="none" stroke="#ffffff" stroke-width="12"/>
      </svg>
    </div>
    <svg class="panel-tail" width="22" height="32" viewBox="0 0 22 32" aria-hidden="true">
      <polygon points="0,0 21,0 0,30" fill="var(--brand-blue)"/>
    </svg>

    <h1 class="brand-text company-name">Vormley's Clerical</h1>
    <p class="brand-text tagline">Providing Balanced Efficient Support</p>

    <div class="contact-block">
      <p class="person-name">Ilsa Vormley</p>
      <p class="contact-line">
        <svg class="contact-icon" width="9" height="14" viewBox="0 0 9 14" aria-hidden="true">
          <path d="M1.5 0h6A1.5 1.5 0 0 1 9 1.5v11A1.5 1.5 0 0 1 7.5 14h-6A1.5 1.5 0 0 1 0 12.5v-11A1.5 1.5 0 0 1 1.5 0zM1.5 2v9h6V2z"/>
        </svg>
        <span>0418 571 924</span>
      </p>
      <p class="contact-line">
        <svg class="contact-icon" width="14" height="14" viewBox="0 0 14 14" aria-hidden="true">
          <rect x="0" y="1" width="4" height="12" rx="1.5"/>
          <path d="M5 2h8a1 1 0 0 1 1 1v9a1 1 0 0 1-1 1H5zM7 4v2h5V4zM7 8v1.5h1.5V8zM10 8v1.5h1.5V8zM7 10.5V12h1.5v-1.5zM10 10.5V12h1.5v-1.5z"/>
        </svg>
        <span>02 6519 4027</span>
      </p>
      <p class="contact-line">
        <svg class="contact-icon" width="16" height="11" viewBox="0 0 16 11" aria-hidden="true">
          <path d="M0 0h16v1.2L8 6.5 0 1.2z"/>
          <path d="M0 2.6l8 5.3 8-5.3V11H0z"/>
        </svg>
        <span>vormleysclerical@plimmet.com.au</span>
      </p>
    </div>
  </div>
</body>
</html>
```